Business Card Design

Just looking for a good designs that looks good with our company logo. I'd like it to be simple and to the point. Just including contact information, our logo, and my name somewhere on the card so future clients know who they're contacting, and a couple services offered. The two images I attached are pictures of our logo. I don't care which color they they are, I just attached both images to give a reference of logo colors depending on the color of the card.
Names: Derek Hallory
Phone: 816-442-7061
Email: greenvalebrush@mailzen.test
Services offered:
Mowing
Fertilization
Aeration
Bed & tree maintenance
and more.
Industry/Entity Type
Business
Contact Information for Business Card
Names: Derek Hallory
Phone: 816-442-7061
Look and feel

```html
<!DOCTYPE html>
<html lang="en">
<head>
<meta charset="utf-8">
<title>Greenvale Lawn – Business Card</title>
<link href="https://fonts.googleapis.com/css2?family=Arimo:wght@400;700&display=swap" rel="stylesheet">
<style>
  :root {
    --page: #d9d2c8;
    --card: #231f20;
    --accent: #e8452c;
    --text: #ffffff;
    --muted: #a7a9ac;
  }
  html, body {
    margin: 0;
    width: 1200px;
    height: 800px;
    overflow: hidden;
    background: var(--page);
    font-family: "Arimo", Arial, sans-serif;
  }
  .card {
    position: absolute;
    left: 110px;
    top: 143px;
    width: 980px;
    height: 514px;
    background: var(--card);
    color: var(--text);
    box-shadow: 0 10px 30px rgba(0,0,0,.25);
  }
  .brand {
    position: absolute;
    left: 70px;
    top: 95px;
    width: 420px;
    display: flex;
    align-items: center;
    gap: 14px;
  }
  .brand-dot {
    flex: none;
    width: 40px;
    height: 40px;
    border-radius: 50%;
    background: var(--accent);
  }
  .brand-name {
    font-size: 36px;
    font-weight: 700;
    color: var(--muted);
    letter-spacing: 1px;
    white-space: nowrap;
  }
  .tagline {
    position: absolute;
    left: 140px;
    top: 185px;
    font-size: 26px;
    line-height: 1.5;
  }
  .tagline .quality { color: var(--text); }
  .tagline .licensed { color: var(--accent); margin-top: 10px; }
  .contact {
    position: absolute;
    left: 580px;
    top: 90px;
    font-size: 22px;
  }
  .contact .name {
    color: var(--accent);
    font-weight: 700;
    font-size: 30px;
    margin-bottom: 10px;
  }
  .contact .row {
    display: flex;
    align-items: center;
    gap: 10px;
    margin-top: 6px;
    white-space: nowrap;
  }
  .contact svg { flex: none; }
  .services {
    position: absolute;
    left: 0;
    right: 0;
    bottom: 70px;
    text-align: center;
    font-size: 25px;
    line-height: 1.25;
  }
  .services .sep { color: var(--accent); margin: 0 6px; }
</style>
</head>
<body>
  <div class="card">
    <div class="brand">
      <span class="brand-dot"></span>
      <span class="brand-name">GREENVALE LAWN</span>
    </div>
    <div class="tagline">
      <div class="quality">Quality Guaranteed</div>
      <div class="licensed">Licensed &amp; Insured</div>
    </div>
    <div class="contact">
      <div class="name">Derek Hallory</div>
      <div class="row">
        <svg width="20" height="20" viewBox="0 0 20 20" aria-hidden="true">
          <rect x="4" y="1.5" width="12" height="17" rx="2" fill="none" stroke="#e8452c" stroke-width="2"/>
          <line x1="7" y1="6" x2="13" y2="6" stroke="#e8452c" stroke-width="1.5"/>
          <circle cx="10" cy="15" r="1.2" fill="#e8452c"/>
        </svg>
        <span>: 816-442-7061</span>
      </div>
      <div class="row">
        <svg width="24" height="18" viewBox="0 0 24 18" aria-hidden="true">
          <rect x="1" y="1" width="22" height="16" fill="none" stroke="#e8452c" stroke-width="2"/>
          <polyline points="1,1 12,10 23,1" fill="none" stroke="#e8452c" stroke-width="2"/>
        </svg>
        <span>: greenvalebrush@mailzen.test</span>
      </div>
    </div>
    <div class="services">
      Mowing<span class="sep">|</span>Fertilization<span class="sep">|</span>Aeration<span class="sep">|</span>Bed &amp; Tree maintenance<span class="sep">|</span>Snow removal<br>
      and more...
    </div>
  </div>
</body>
</html>
```